Utility Contractor looking for a new website

Water and wastewater utility contractor looking to create a new website that highlights our various services. We are looking for modern web presence that can be updated with current projects and new services as we grow. We have an existing logo that we would like to incorporate into the overall design of the site
Updates

Hi, Thank you for all the design submissions. I have had some time to review and have eliminated the ones I feel are not what I am looking for. Based on the designs that remain, I am looking for a clean (not to many bold colours), modern look that is not to busy (long scrolling page), Thanks, Owen

Target Market(s)

project managers, strata boards, owners, people who make decisions as to who operates their water/wastewater system

Industry/Entity Type

Utility

Font styles to use
Sans Serif

Requirements
Must have
• A min page that describes the company and what we do, A page for each of our services that outlines the service and the benefits of it. the look must be consistent throughout. additionally each service page should have some images related to the service

```html
<!DOCTYPE html>
<html lang="en">
<head>
<meta charset="utf-8">
<title>Clearline Utilities Ltd.</title>
<link rel="stylesheet" href="https://fonts.googleapis.com/css2?family=Hind:wght@300;400;500;600&family=Montserrat:wght@500&display=swap">
<style>
:root{
  --navy:#0f2a4a;
  --green:#14a04a;
  --green-dark:#0d8a3c;
  --sky:#1aa7dc;
  --blue-top:#00b9e6;
  --blue-bottom:#0a8ad4;
  --text:#6b6b6b;
  --white:#fff;
  --footer:#0b2546;
}
*{box-sizing:border-box;margin:0;padding:0}
html,body{width:771px;height:1200px;overflow:hidden;background:var(--white)}
body{font-family:"Hind",sans-serif;color:var(--text);position:relative}
.site-header{height:74px;position:relative}
.brand{position:absolute;left:78px;top:24px;display:flex;align-items:center;gap:8px;font-weight:600;font-size:20px;line-height:1;color:var(--navy);letter-spacing:.5px}
.brand-dot{width:14px;height:14px;border-radius:50%;background:var(--sky)}
.support{position:absolute;right:75px;top:32px;text-align:right}
.support-label{font-size:11px;color:var(--sky)}
.support-phone{font-size:16px;color:var(--navy);margin-top:1px}
.main-nav{height:32px;background:linear-gradient(var(--green),var(--green-dark));display:flex;justify-content:center}
.main-nav a{color:var(--white);text-decoration:none;font-size:11px;font-weight:500;line-height:32px;padding:0 13px;border-left:1px solid rgba(0,0,0,.12)}
.main-nav a:first-child{border-left:none}
.hero{height:296px;position:relative;background:linear-gradient(#d9dfe2 0%,#c9d2d6 38%,#6e9a4c 55%,#4f8a33 75%,#b9c6cc 88%,#7f9f5c 100%)}
.hero-title{position:absolute;left:72px;top:118px;font-family:"Montserrat",sans-serif;color:#111;line-height:1}
.hero-title .line1{font-size:19px}
.hero-title .line2{font-size:25px;margin-top:6px}
.dots{position:absolute;left:361px;top:281px;display:flex;gap:3px}
.dots span{width:9px;height:9px;border-radius:50%;background:#1a1a1a}
.dots span:first-child{background:var(--sky)}
.intro{text-align:center;padding-top:25px}
.intro h1{font-weight:300;font-size:24px;color:var(--navy)}
.intro p{font-size:9px;font-weight:300;width:560px;margin:6px auto 0;line-height:1.5}
.features{display:flex;gap:0;position:absolute;top:524px;left:75px}
.feature{display:flex;gap:8px;width:215px}
.feature-img{width:78px;height:70px;border-radius:2px;flex:none}
.feature h3{font-weight:300;font-size:14px;color:var(--sky);line-height:1;margin-top:2px}
.feature p{font-size:8px;font-weight:300;line-height:1.6;margin-top:5px;width:115px}
.feature a{display:block;font-size:7.5px;font-weight:600;color:var(--navy);text-decoration:none;margin-top:4px}
.services{position:absolute;top:642px;left:0;width:771px;height:266px;background:linear-gradient(var(--blue-top),var(--blue-bottom));text-align:center;color:var(--white)}
.services h2{font-weight:300;font-size:22px;margin-top:27px}
.services > p{font-size:8.5px;font-weight:300;width:560px;margin:4px auto 0;line-height:1.55}
.service-grid{display:flex;justify-content:center;gap:27px;margin-top:20px}
.service{width:126px}
.service svg{height:50px}
.service h3{font-weight:400;font-size:12px;margin-top:6px}
.service p{font-size:8px;font-weight:300;line-height:1.55}
.service a{display:block;font-size:8px;font-weight:600;color:var(--white);text-decoration:none;margin-top:3px}
.testimonials{position:absolute;top:940px;left:0;width:771px;text-align:center}
.testimonials h2{font-weight:300;font-size:22px;color:var(--green)}
.quotes{display:flex;justify-content:center;gap:38px;margin-top:12px}
.quote{width:232px}
.quote p{font-size:9px;font-style:italic;font-weight:300;line-height:1.55}
.author{display:flex;align-items:center;gap:5px;margin:5px 0 0 59px;text-align:left}
.avatar{width:37px;height:37px;border-radius:50%;background:radial-gradient(#c9b29c,#6d7f5e)}
.author strong{display:block;font-size:9.5px;font-weight:500;color:#222}
.author span{font-size:8px;color:#444}
.site-footer{position:absolute;top:1118px;left:0;width:771px;height:82px;background:var(--footer);color:var(--white)}
.footer-nav{position:absolute;left:79px;top:24px;font-size:8.5px;font-weight:500}
.footer-nav a{color:var(--white);text-decoration:none}
.footer-nav i{font-style:normal;margin:0 5px}
.copyright{position:absolute;left:79px;top:46px;font-size:8px;font-weight:300;color:#cdd6e2}
.social{position:absolute;right:76px;top:20px;display:flex;gap:3px}
.social span{width:17px;height:17px;border-radius:50%;background:var(--white)}
</style>
</head>
<body>
<header class="site-header">
  <div class="brand"><span class="brand-dot"></span>CLEARLINE UTILITIES LTD.</div>
  <div class="support"><div class="support-label">Phone Support</div><div class="support-phone">604.555.0187</div></div>
</header>
<nav class="main-nav">
  <a href="#">HOME</a><a href="#">ABOUT US</a><a href="#">SERVICES</a><a href="#">WATER PROJECTS</a><a href="#">MISSION</a><a href="#">BLOG</a><a href="#">TESTIMONIALS</a><a href="#">CONTACT</a>
</nav>
<section class="hero" role="img" aria-label="Flooded green meadow with a river weir and bare trees under a grey sky">
  <div class="hero-title"><div class="line1">CURABITUR IACULIS TEMPUS EROS</div><div class="line2">VIVAMUS PORTTITOR VOLUTPAT</div></div>
  <div class="dots"><span></span><span></span><span></span><span></span></div>
</section>
<section class="intro">
  <h1>Mauris nunc quam venenatis nec euismod</h1>
  <p>Phasellus felis dolor scelerisque a tempus eget lobortis id libero Aliquam nec erat at purus cursus interdum Vestibulum ligula augue bibendum accumsan vestibulum ut commodo a mi Morbi ornare gravida elit Integer congue augue et malesuada iaculis ipsum dui aliquet felis</p>
</section>
<div class="features">
  <div class="feature">
    <div class="feature-img" role="img" aria-label="Lit fountain at dusk" style="background:linear-gradient(#5a6f95,#b7c0d4 60%,#3b4a6a)"></div>
    <div><h3>What We Do</h3><p>Phasellus felis dolor sceleris-que a tempus eget lobortis id libero Aliquam nec erat</p><a href="#">LEARN MORE</a></div>
  </div>
  <div class="feature">
    <div class="feature-img" role="img" aria-label="Green pump equipment on grass" style="background:linear-gradient(#7ea75a,#2f6a3a 60%,#6c8f47)"></div>
    <div><h3>How it Works</h3><p>Phasellus felis dolor sceleris-que a tempus eget lobortis id libero Aliquam nec erat</p><a href="#">LEARN MORE</a></div>
  </div>
  <div class="feature">
    <div class="feature-img" role="img" aria-label="Field worker standing on machinery" style="background:linear-gradient(#8fb6de,#5f7fa8 55%,#7a9a4f)"></div>
    <div><h3>Field Crews</h3><p>Phasellus felis dolor sceleris-que a tempus eget lobortis id libero Aliquam nec erat</p><a href="#">LEARN MORE</a></div>
  </div>
</div>
<section class="services">
  <h2>Services We Provide</h2>
  <p>Curabitur tristique mi condimentum orci Phasellus pellentesque aliquam enim Proin dui lectus cursus eu mattis laoreet viverra sit amet quam Curabitur vel dolor ultrices ipsum dictum tristique Praesent vitae lacus Ut velit enim ves</p>
  <div class="service-grid">
    <div class="service">
      <svg viewBox="0 0 50 50" width="50"><circle cx="25" cy="22" r="20" fill="none" stroke="#fff" stroke-width="3"/><rect x="23" y="22" width="4" height="27" fill="#fff"/><ellipse cx="18" cy="20" rx="5" ry="8" fill="#fff"/><ellipse cx="32" cy="20" rx="5" ry="8" fill="#fff"/><ellipse cx="25" cy="12" rx="4" ry="6" fill="#fff"/></svg>
      <h3>Featured Service</h3><p>Phasellus felis dolor scelerisque a tempus eget lobortis id libero</p><a href="#">LERAN MORE</a>
    </div>
    <div class="service">
      <svg viewBox="0 0 50 50" width="50"><path d="M8 26 25 10 42 26" fill="none" stroke="#fff" stroke-width="3"/><rect x="14" y="24" width="22" height="12" fill="#fff"/><rect x="22" y="28" width="6" height="8" fill="#0aa4de"/><path d="M6 41q5-4 10 0t10 0 10 0 10 0M6 47q5-4 10 0t10 0 10 0 10 0" fill="none" stroke="#fff" stroke-width="2.5"/></svg>
      <h3>Featured Service</h3><p>Phasellus felis dolor scelerisque a tempus eget lobortis id libero</p><a href="#">LERAN MORE</a>
    </div>
    <div class="service">
      <svg viewBox="0 0 50 50" width="50"><path d="M20 18 18 46h5l-1-28z" fill="#fff"/><path d="M20 17 17 2M20 17 6 26M20 17 34 22" stroke="#fff" stroke-width="3"/><path d="M38 30 37 46h3l-1-16z" fill="#fff"/><path d="M38 30 37 22M38 30 31 35M38 30 45 33" stroke="#fff" stroke-width="2"/><path d="M4 47h44" stroke="#fff" stroke-width="2"/></svg>
      <h3>Featured Service</h3><p>Phasellus felis dolor scelerisque a tempus eget lobortis id libero</p><a href="#">LERAN MORE</a>
    </div>
    <div class="service">
      <svg viewBox="0 0 50 50" width="50"><path d="M25 6C20 17 11 25 11 33a14 14 0 0 0 28 0C39 25 30 17 25 6z" fill="#fff"/></svg>
      <h3>Featured Service</h3><p>Phasellus felis dolor scelerisque a tempus eget lobortis id libero</p><a href="#">LERAN MORE</a>
    </div>
  </div>
</section>
<section class="testimonials">
  <h2>What People Saying</h2>
  <div class="quotes">
    <div class="quote">
      <p>Vivamus porttitor neque at volutpat rutrum purus nisi eleif-end libero a tempus libero lectus feugiat felis Morbi diam mauris viverra in gravida eu mattis in ante</p>
      <div class="author"><div class="avatar" role="img" aria-label="Author portrait"></div><div><strong>By Author Name</strong><span>Location/Area</span></div></div>
    </div>
    <div class="quote">
      <p>Maecenas at justo id velit placerat molestie Donec dictum lectus non odio Cras a ante vitae enim iaculis aliquam Mauris nunc quam venenatis nec euismod</p>
      <div class="author"><div class="avatar" role="img" aria-label="Author portrait" style="background:radial-gradient(#d8b49c,#3b2a24)"></div><div><strong>By Author Name</strong><span>Location/Area</span></div></div>
    </div>
  </div>
</section>
<footer class="site-footer">
  <nav class="footer-nav"><a href="#">HOME</a><i>|</i><a href="#">VOICE LESSONS</a><i>|</i><a href="#">BLOG</a><i>|</i><a href="#">WHAT STUDENTS SAY</a><i>|</i><a href="#">MEET THE INSTRUCTORS</a><i>|</i><a href="#">VOICE BREAKTHROUGH</a></nav>
  <div class="copyright">© 2014 Company Name &nbsp;All right reserved &nbsp;Term of Use</div>
  <div class="social"><span></span><span></span><span></span><span></span></div>
</footer>
</body>
</html>
```